Vellora Labs - Mushroom Supplement Packaging

Our brand is called Vellora Labs. I've added a couple different logos that you can use. We are creating a line up of Mushroom Supplement products. I will add the entire line-up of products here. I've added examples of other products and packaging shape types I can purchase. Give me different options for packaging that is minimalist and clean for this brand that makes it look really well made and clean and make people want to buy.

Product 1 Lions Mane 1g
Product 2 Cordyceps 1g
Product 3 Chaga 1g
Product 4 Turkey Tail 1g
Product 5 Reishi 1g
Product 6 Maitake 1g
Product 7 Shiitake 1g

Product 8 (Mix) Lions Mane 143mg
Cordyceps 143mg
Chaga 143mg
Turkey Tail 143mg
Reishi 143mg
Maitake 143mg
Shiitake 143mg

```html
<!DOCTYPE html>
<html lang="en">
<head>
<meta charset="utf-8">
<title>Vellora Labs – Lions Mane Label</title>
<link href="https://fonts.googleapis.com/css2?family=Outfit:wght@300;400;500;600;700&display=swap" rel="stylesheet">
<style>
  :root {
    --page-bg: #efefef;
    --green-deep: #4b7150;
    --green-light: #86a38a;
    --gold: #e9b824;
    --gold-light: #f3d56a;
    --white: #ffffff;
    --panel-light: #f4f4f4;
    --panel-shade: #dcdcdc;
    --ink: #2b2b2b;
    --rule-dark: #2f4a33;
  }
  * { margin: 0; padding: 0; box-sizing: border-box; }
  html, body {
    width: 1200px; height: 1200px; overflow: hidden;
    background: var(--page-bg);
    font-family: "Outfit", sans-serif;
  }
  .label {
    position: absolute;
    left: 166px; top: 120px;
    width: 867px; height: 960px;
    overflow: hidden;
  }
  .label-bg { position: absolute; inset: 0; }
  .count {
    position: absolute; left: 727px; top: 56px; width: 100px;
    text-align: center; color: var(--ink);
  }
  .count-number { font-size: 66px; font-weight: 700; line-height: 1; letter-spacing: -1px; }
  .count-unit { font-size: 11px; font-weight: 500; letter-spacing: 0.2px; margin-top: 2px; }
  .brand {
    position: absolute; left: 59px; top: 178px;
    color: var(--white); font-weight: 600; text-transform: uppercase;
    line-height: 0.95;
  }
  .brand-name { font-size: 64px; letter-spacing: 1px; }
  .brand-sub { font-size: 40px; letter-spacing: 6px; padding-left: 4px; }
  .product-name {
    position: absolute; left: 50px; top: 402px;
    font-size: 98px; font-weight: 600; color: var(--gold);
    letter-spacing: -1px; white-space: nowrap;
  }
  .title-rule {
    position: absolute; left: 43px; top: 528px;
    width: 663px; height: 2px; background: var(--gold);
  }
  .product-type {
    position: absolute; left: 55px; top: 540px;
    font-size: 30px; font-weight: 600; color: var(--white);
    letter-spacing: -0.3px;
  }
  .benefits {
    position: absolute; left: 54px; top: 636px;
    font-size: 31px; font-weight: 400; color: var(--white);
    line-height: 1.42; letter-spacing: -0.3px;
  }
  .supplement-note {
    position: absolute; left: 54px; top: 798px;
    font-size: 24px; font-weight: 400; color: var(--white);
    letter-spacing: -0.2px;
  }
  .note-rule {
    position: absolute; left: 51px; top: 846px;
    width: 130px; height: 4px; background: var(--rule-dark);
  }
  .net-content {
    position: absolute; left: 54px; top: 864px;
    font-size: 32px; color: var(--white); letter-spacing: -0.5px;
  }
  .net-content strong { font-weight: 700; }
  .net-content span { font-weight: 400; }
  .mushroom-art {
    position: absolute; left: 608px; top: 670px;
    width: 256px; height: 288px;
    background: radial-gradient(ellipse at 50% 45%, #cfcfcf 0%, #e2e2e2 60%, rgba(230,230,230,0) 100%);
  }
</style>
</head>
<body>
  <div class="label">
    <svg class="label-bg" width="867" height="960" viewBox="0 0 867 960">
      <defs>
        <linearGradient id="panelShade" x1="0" y1="0" x2="1" y2="1">
          <stop offset="0" stop-color="#f6f6f6"/>
          <stop offset="1" stop-color="#dadada"/>
        </linearGradient>
        <linearGradient id="greenField" x1="0" y1="0" x2="1" y2="0.4">
          <stop offset="0" stop-color="#4a7050"/>
          <stop offset="0.55" stop-color="#86a38a"/>
          <stop offset="1" stop-color="#4f7654"/>
        </linearGradient>
        <linearGradient id="goldEdge" x1="0" y1="0" x2="0" y2="1">
          <stop offset="0" stop-color="#e9b824"/>
          <stop offset="0.5" stop-color="#f5d974"/>
          <stop offset="1" stop-color="#e9b824"/>
        </linearGradient>
      </defs>
      <rect width="867" height="960" fill="url(#panelShade)"/>
      <path d="M0 0 H420 Q452 0 468 28 L728 488 Q740 508 728 528 L405 960 H0 Z" fill="url(#greenField)"/>
      <path d="M420 0 Q452 0 468 28 L728 488 Q740 508 728 528 L405 960" fill="none" stroke="url(#goldEdge)" stroke-width="7"/>
    </svg>

    <div class="count">
      <div class="count-number">60</div>
      <div class="count-unit">CAPSULES</div>
    </div>

    <div class="brand">
      <div class="brand-name">Vellora</div>
      <div class="brand-sub">Labs</div>
    </div>

    <div class="product-name">LIONS MANE</div>
    <div class="title-rule"></div>
    <div class="product-type">MUSHROOM EXTRACT CAPSULES</div>

    <div class="benefits">Energy Support &amp; Immune<br>Balancing Properties</div>

    <div class="supplement-note">DIETARY SUPPLEMENT</div>
    <div class="note-rule"></div>
    <div class="net-content"><strong>2fl oz</strong> <span>/ 60g</span></div>

    <div class="mushroom-art" role="img" aria-label="Line illustration of a cluster of mushrooms"></div>
  </div>
</body>
</html>
```